Physical Large Banner For Corporate Event

Hi, we would like a large banner designed for a corporate event using adobe illustrator/pdf. The size of the banner must be 2000 (h)x800 (w) mm to fit with the printing requirements (please visit https://www.inkvaleprints.com/products/48/banner-stands and see the guidelines for size for a standard banner)

Our organisation holds events for students to find out more on top careers such as Investment Banking & Law. The banner design can be fairly simple but bold using the same themes and colours on our website www.brightlanefutures.co.uk. We can provide imagery of our logo for use/other pictures requested such as those for students/cityscapes etc.

The only text on the banner should be our web address at the bottom (www.brightlanefutures.co.uk) and a line that says "A Head Start in the City, We bring the internship to you..." like in our website homepage.

Target Market(s)

Students & Graduate Recruiters

Industry/Entity Type

Education

Requirements
Must have
• Website address
• Cool imagery
Should not have
• Too much clutter, clean and simple pleaseE

```html
<!DOCTYPE html>
<html lang="en">
<head>
<meta charset="utf-8">
<title>Brightlane – A Head Start in the City</title>
<link rel="stylesheet" href="https://fonts.googleapis.com/css2?family=Comfortaa:wght@400;700&family=Tinos&display=swap">
<style>
  :root {
    --ink-grey: #4a4a4a;
    --brand-red: #8c1217;
    --band-red: #9b1016;
    --band-red-dark: #6d0a0e;
    --header-top: #f7f7f7;
    --header-bottom: #dedede;
    --footer-top: #f4f4f4;
    --footer-bottom: #d6d6d6;
    --rule-dark: #3a3a3a;
    --url-bar: #3d3d3d;
    --url-bar-edge: #2a2a2a;
    --url-text: #f2f2f2;
    --photo-green: #7f9a4a;
    --photo-mid: #6f6a62;
    --photo-dark: #3d3b3a;
  }
  html, body {
    margin: 0;
    padding: 0;
    overflow: hidden;
    background: #ffffff;
  }
  .banner {
    position: relative;
    width: 1200px;
    height: 3000px;
    overflow: hidden;
    background: linear-gradient(to bottom, var(--footer-top), var(--footer-bottom));
  }
  .header {
    position: absolute;
    left: 0; top: 0;
    width: 1200px;
    height: 695px;
    background: linear-gradient(to bottom, var(--header-top), var(--header-bottom));
    border-bottom: 6px solid var(--rule-dark);
  }
  .headline {
    position: absolute;
    left: 125px;
    top: 95px;
    margin: 0;
    font-family: "Comfortaa", sans-serif;
    font-weight: 400;
    font-size: 100px;
    line-height: 125px;
    color: var(--ink-grey);
    letter-spacing: 1px;
  }
  .headline strong { font-weight: 700; }
  .tagline {
    position: absolute;
    left: 130px;
    top: 455px;
    margin: 0;
    font-family: "Comfortaa", sans-serif;
    font-weight: 400;
    font-size: 66px;
    line-height: 125px;
    color: var(--brand-red);
  }
  .tagline strong {
    font-weight: 700;
    font-size: 88px;
  }
  .hero-photo {
    position: absolute;
    left: 0; top: 701px;
    width: 1200px;
    height: 1700px;
    background:
      radial-gradient(ellipse 520px 700px at 800px 900px, var(--photo-mid), transparent 75%),
      linear-gradient(to bottom, var(--photo-green) 0%, #8da85a 30%, var(--photo-mid) 60%, var(--photo-dark) 100%);
  }
  .swoosh {
    position: absolute;
    left: 0; top: 1950px;
    width: 1200px;
    height: 600px;
  }
  .brand {
    position: absolute;
    left: 120px;
    top: 2560px;
    display: flex;
    align-items: center;
    gap: 30px;
  }
  .brand-mark {
    width: 60px;
    height: 60px;
    background: var(--brand-red);
  }
  .brand-name {
    font-family: "Tinos", serif;
    font-size: 118px;
    line-height: 1;
    color: var(--ink-grey);
  }
  .url-bar {
    position: absolute;
    left: 0; top: 2780px;
    width: 1075px;
    height: 120px;
    background: linear-gradient(to bottom, var(--url-bar), var(--url-bar-edge));
    display: flex;
    align-items: center;
    justify-content: center;
    font-family: "Tinos", serif;
    font-size: 64px;
    color: var(--url-text);
  }
</style>
</head>
<body>
  <main class="banner">
    <header class="header">
      <h1 class="headline">A <strong>Head Start</strong><br>in the City,</h1>
      <p class="tagline">We bring the<br><strong>internship</strong> to you...</p>
    </header>

    <div class="hero-photo" role="img" aria-label="Photograph of smiling students outdoors in front of green trees, one in front holding a red book and wearing a backpack"></div>

    <svg class="swoosh" viewBox="0 0 1200 600" preserveAspectRatio="none" aria-hidden="true">
      <defs>
        <linearGradient id="bandGradient" x1="0" y1="0" x2="1" y2="0">
          <stop offset="0" stop-color="var(--band-red-dark)"/>
          <stop offset="0.5" stop-color="var(--band-red)"/>
          <stop offset="1" stop-color="var(--band-red-dark)"/>
        </linearGradient>
        <linearGradient id="footerGradient" x1="0" y1="0" x2="0" y2="1">
          <stop offset="0" stop-color="#fafafa"/>
          <stop offset="1" stop-color="#eeeeee"/>
        </linearGradient>
      </defs>
      <path class="swoosh-band" d="M0,80 C400,140 800,220 1200,300 L1200,460 C800,330 400,175 0,125 Z" fill="url(#bandGradient)"/>
      <path class="swoosh-base" d="M0,125 C400,175 800,330 1200,460 L1200,600 L0,600 Z" fill="url(#footerGradient)"/>
    </svg>

    <div class="brand">
      <span class="brand-mark"></span>
      <span class="brand-name">Brightlane</span>
    </div>

    <div class="url-bar">www.brightlanefutures.co.uk</div>
  </main>
</body>
</html>
```